Design a modern, classy & professional business card for an online real estate agency, specializing in medium-luxury properties in Thailand and later in Singapore and UK.

Possible design ideas so far: (not essential)

- curved corner(s) to the card, white on front & turquoise on back or visa versa.

- front of card - clear and simple, company name in metallic grey/monochrome, logo graphic & company name on front in spot UV or embossed/debossed effect.

- back of card - large, close-cropped, 'ghost' patterns of the C-shaped curves of logo, or company name repeated on back of card in spot UV.

Target Market(s)

- young to middle-aged professionals mainly (but ideally should design should suit all)

- UK, US,EU,AUS & ASIAN mainly (but ideally should design should suit all countries)

Industry/Entity Type

Real Estate

Requirements
Must have
• THEME:
- Luxurious & Modern
- Clean & striking
- Unique & creative

INFO:
- Logo & company name on front
- Contact details on back:

Tobias Lindqvar
Managing Director

www.velmoraestates.example
www.velmoraestates-uk.example

Tel: 084-273-6190
email: tobias@velmoraestates.example

(contact details can be displayed in any order as suites design.)

Nice to have
• - curved corner(s) to the card, white on front & turquoise on back or visa versa.

Should not have
• - No generic images of properties, palm trees/coconut trees etc.

- No other other bold colors, except for main turquoise, grey, metallic white & black theme.

- No obvious business card templates

```html
<!DOCTYPE html>
<html lang="en">
<head>
<meta charset="utf-8">
<title>Velmora Estates – Business Card</title>
<link rel="stylesheet" href="https://fonts.googleapis.com/css2?family=Arimo:wght@400&family=Tinos:wght@400&display=swap">
<style>
  :root {
    --stage-glow: #3f5c99;
    --stage-mid: #1c2540;
    --stage-edge: #07080c;
    --card-white: #ffffff;
    --turquoise: #14c8c2;
    --turquoise-light: #6fdedb;
    --turquoise-pale: #a9ece9;
    --brand-grey: #707070;
    --name-grey: #484848;
    --ink: #111111;
    --rule: #2b4a4a;
  }
  * { box-sizing: border-box; margin: 0; padding: 0; }
  html, body {
    width: 1200px;
    height: 889px;
    overflow: hidden;
  }
  body {
    position: relative;
    background: radial-gradient(ellipse 620px 520px at 470px 420px,
      var(--stage-glow) 0%, var(--stage-mid) 55%, var(--stage-edge) 100%);
    font-family: "Arimo", Arial, sans-serif;
  }

  .card {
    position: absolute;
    width: 710px;
    height: 405px;
    overflow: hidden;
  }

  /* Front */
  .card--front {
    left: 85px;
    top: 38px;
    background: var(--card-white);
    border-radius: 88px 0 115px 0;
  }
  .brand {
    position: absolute;
    display: flex;
    align-items: center;
  }
  .brand__square {
    flex: none;
    background: var(--turquoise);
  }
  .brand__name {
    font-family: "Tinos", "Times New Roman", serif;
    font-weight: 400;
    color: var(--brand-grey);
    line-height: 1;
  }
  .brand__word {
    display: block;
  }
  .brand__sub {
    display: block;
    text-transform: uppercase;
  }

  .card--front .brand { left: 143px; top: 144px; }
  .card--front .brand__square { width: 120px; height: 120px; margin-right: 16px; }
  .card--front .brand__word { font-size: 80px; letter-spacing: -1px; }
  .card--front .brand__sub { font-size: 27px; letter-spacing: 5.2px; margin-top: 6px; padding-left: 4px; }

  /* Back */
  .card--back {
    left: 427px;
    top: 425px;
    width: 708px;
    background: var(--turquoise);
    border-radius: 96px 0 106px 0;
  }
  .card__texture {
    position: absolute;
    inset: 0;
    background:
      linear-gradient(160deg, var(--turquoise-pale) 0%, rgba(169,236,233,0) 45%),
      linear-gradient(20deg, var(--turquoise) 30%, var(--turquoise-light) 100%);
    opacity: 0.9;
  }
  .card--back .brand { left: 354px; top: 26px; }
  .card--back .brand__square { width: 90px; height: 90px; margin-right: 12px; }
  .card--back .brand__word { font-size: 58px; letter-spacing: -0.5px; }
  .card--back .brand__sub { font-size: 19px; letter-spacing: 3.6px; margin-top: 5px; padding-left: 3px; }

  .holder {
    position: absolute;
    left: 0;
    right: 0;
    top: 182px;
    text-align: center;
    padding-left: 76px;
  }
  .holder__name {
    font-family: "Arimo", Arial, sans-serif;
    font-size: 40px;
    font-weight: 400;
    color: var(--name-grey);
    line-height: 1.1;
  }
  .holder__role {
    font-family: "Tinos", "Times New Roman", serif;
    font-size: 26px;
    color: var(--ink);
    margin-top: 0;
    padding-right: 20px;
  }

  .contacts {
    position: absolute;
    left: 39px;
    top: 311px;
    width: 600px;
    border-top: 1px solid var(--rule);
    border-bottom: 1px solid var(--rule);
    padding: 8px 0 9px 1px;
    display: flex;
    justify-content: space-between;
    font-size: 17.5px;
    line-height: 24px;
    color: var(--ink);
  }
  .contacts__label { display: inline-block; width: 52px; }
  .contacts__label--email { width: auto; }
  .contacts__web { padding-right: 22px; }
</style>
</head>
<body>

  <section class="card card--front" aria-label="Business card front">
    <div class="brand">
      <span class="brand__square"></span>
      <span class="brand__name">
        <span class="brand__word">Velmora</span>
        <span class="brand__sub">Estates</span>
      </span>
    </div>
  </section>

  <section class="card card--back" aria-label="Business card back">
    <div class="card__texture" role="img" aria-label="Large faint turquoise curved brand pattern across the card"></div>

    <div class="brand">
      <span class="brand__square"></span>
      <span class="brand__name">
        <span class="brand__word">Velmora</span>
        <span class="brand__sub">Estates</span>
      </span>
    </div>

    <div class="holder">
      <h1 class="holder__name">Tobias Lindqvar</h1>
      <p class="holder__role">Managing Director</p>
    </div>

    <div class="contacts">
      <div class="contacts__direct">
        <div><span class="contacts__label">Tel</span>: 084-273-6190</div>
        <div><span class="contacts__label contacts__label--email">email</span> : tobias@velmoraestates.example</div>
      </div>
      <div class="contacts__web">
        <div>www.velmoraestates.example</div>
        <div>www.velmoraestates-uk.example</div>
      </div>
    </div>
  </section>

</body>
</html>
```